Companybrochure for Consulting & Financing Firm

I need to have a Company Brochure asap for our company. We have a website that describes what we do, but we need also a brochure, that can be sent by PDF of eventually be printed as well.

The brochure should be short but nice and appealing to the customers.

We provide professional management consulting and help our customers to get finance for very diferent projects. Our business has a lot to do with personal relations, but also we are very professional in the way we work and how develop the solutions for our clients. Our clients are mainly government-owned firm, but also private trading companies and wealthy private investors.

Our customers are mainly in Latin America, but the company is headquater is in Switzerland. We are opening offices in Panama and Caracas, this should be easaly be adabtable later.

Please have a look at our website www.brevalto.ch. In the brochure, we would segment our services in 1.) Project Developments 2.) Management Conulting 3.) Investment Management and 4.) Finance Solutions.

Also do have a look at www.brevalto.ch
(Click E for the English version)

I managed to put the Mock-Up to the Website.
It is actually not really a mock-up, it is a version I have designed myself.
Well as I am not a designer, I hope you can make it much better.
The content however is what I would put in any other design as well.

Target Market(s)

Top Management, Investors, Entrepreneurs, Government Officials

Industry/Entity Type

Management Consulting

Requirements
Must have
• Design should reflect this image elements:

We are entrepreneurs.
We are comitted to get things done.
We work closely with the client side by side.
We are a professional partner.
We are not afraid of delivering unconventional solutions.
We look at the problem from various angles.
We analyse, develop solutions and implent results.
Should not have
• Typical US-American style elements. We do not want to give the impression of being a US company.

We do not want to appear to be neo-liberal. We are a politically neutral professional consulting firm.

```html
<!DOCTYPE html>
<html lang="en">
<head>
<meta charset="utf-8">
<title>Brevalto – Services</title>
<link rel="stylesheet" href="https://fonts.googleapis.com/css2?family=Arimo:wght@400;700&display=swap">
<style>
  :root {
    --canvas: #bcbdbf;
    --panel-body: #d1d2d4;
    --title-band: #e5e6e8;
    --accent-band: #3f4679;
    --title-ink: #333a6e;
    --body-ink: #56585c;
    --link-ink: #2f3a82;
  }
  * { margin: 0; padding: 0; box-sizing: border-box; }
  html, body {
    width: 1200px;
    height: 434px;
    overflow: hidden;
    background: var(--canvas);
    font-family: "Arimo", Arial, sans-serif;
  }
  .spread { position: relative; width: 1200px; height: 434px; }
  .service-panel {
    position: absolute;
    top: 12px;
    width: 578px;
    height: 410px;
    background: var(--panel-body);
  }
  .service-panel--consulting { left: 17px; }
  .service-panel--investment { left: 605px; }
  .service-visual {
    position: absolute;
    left: 0; top: 0;
    width: 100%;
    height: 210px;
  }
  .service-visual--chess {
    background: linear-gradient(100deg, #ffffff 0%, #fbf6ee 25%, #e9c489 45%, #2a2623 55%, #e3b872 68%, #f6e4c2 85%, #ffffff 100%);
  }
  .service-visual--honeycomb {
    background: linear-gradient(120deg, #e6b53a 0%, #b88224 30%, #5a3b16 55%, #c79530 75%, #e8bd48 100%);
  }
  .accent-band {
    position: absolute;
    left: 0; top: 210px;
    width: 100%; height: 14px;
    background: var(--accent-band);
  }
  .title-band {
    position: absolute;
    left: 0; top: 224px;
    width: 100%; height: 41px;
    background: var(--title-band);
  }
  .service-title {
    position: absolute;
    left: 51px; top: 232px;
    font-size: 20px;
    font-weight: 700;
    color: var(--title-ink);
    white-space: nowrap;
  }
  .service-text {
    position: absolute;
    left: 51px; top: 274px;
    font-size: 9.2px;
    line-height: 11.6px;
    color: var(--body-ink);
    white-space: nowrap;
  }
  .service-text p + p { margin-top: 11.6px; }
  .principle { color: var(--link-ink); }
</style>
</head>
<body>
<main class="spread">
  <section class="service-panel service-panel--consulting">
    <div class="service-visual service-visual--chess" role="img" aria-label="Photo of black and wooden chess pieces on a chessboard"></div>
    <div class="accent-band"></div>
    <div class="title-band"></div>
    <h2 class="service-title">&gt;&gt; Management Consulting</h2>
    <div class="service-text">
      <p>We elaborate solutions together with our customers and business partners by assisting<br>
      owners and top management in structured decision making.<br>
      We work goal-oriented following the principle:<br>
      <span class="principle">&gt;Analysis &gt;&gt; Solutions &gt;&gt;&gt; Results.</span></p>
      <p>Our consulting team members do all have many years of experience from previous assignments<br>
      at leading international management consulting companies and are familiar with methodologies<br>
      used in management consulting. We complete the team of consultants with the appropriate subject<br>
      matter experts.</p>
    </div>
  </section>

  <section class="service-panel service-panel--investment">
    <div class="service-visual service-visual--honeycomb" role="img" aria-label="Photo of honey bees working on a golden honeycomb"></div>
    <div class="accent-band"></div>
    <div class="title-band"></div>
    <h2 class="service-title">&gt;&gt; Investment Management</h2>
    <div class="service-text">
      <p>Brevalto has a clear business-like approach to investments. We only engage in those projects or<br>
      companies with which we have a strong relationship.</p>
      <p>That is why we are also willing to take an entrepreneurial risk in the companies we invest in. We participate<br>
      with our own capital and assume functions in the company's management.</p>
      <p>Brevalto currently holds shares in seven SMEs; four of these to 100%. Participation is on equal terms,<br>
      and two of of the companies we are minority shareholders.</p>
    </div>
  </section>
</main>
</body>
</html>
```